Marketing Thornbury

We are a primary school and would like to market our school in a positive light. We have had recent success and would like the local community to know!

Target Market(s)

Parents/Carers in the local community

Industry/Entity Type

School

Font styles to use
Serif

Requirements
Must have
• Thornbury Logo first with our moto 'Growing Bright Minds'

Reference to the fact we are converting to academy status on 1st April 2014 with The Harwick BRIDGE Academy Trust

Reference to the partnership with Colsworth Primary School which has bought recent, quick success

Reference to Edrevue rating of Good. Feb 2014
Nice to have
• School colours dark red

Link to website www.thornburyprimary.example

Link to the academy website www.harwickbridge.example

Statements from Edrevue -

'This is a good school'

'The Executive Headteacher and leadership team have skilfully steered the school's recovery and galvanised staff at all levels to work as a team'

'This is a very different school to the one that existed at the time of the previous inspection'

'Pupils achievement has improved very quickly this year'

'Pupils make a strong start in the school'

'The quality of teaching is good'

'The behaviour of pupils is good'

```html
<!DOCTYPE html>
<html lang="en">
<head>
<meta charset="utf-8">
<title>Growing Bright Minds – Thornbury School flyer</title>
<link rel="stylesheet" href="https://fonts.googleapis.com/css2?family=Roboto+Condensed:wght@700&family=Open+Sans:wght@400;600;700&display=swap">
<style>
  :root {
    --maroon: #7b1b22;
    --maroon-deep: #5e1218;
    --sky-top: #ffffff;
    --sky-bottom: #aebdd6;
    --ink: #111111;
    --ink-soft: #3a3a3a;
    --gold: #f6b51c;
    --white: #ffffff;
    --blush: #f1d9d9;
    --swoosh: #8e949b;
    --swoosh-light: #d3d7dc;
  }
  * { box-sizing: border-box; margin: 0; padding: 0; }
  html, body {
    width: 947px; height: 1200px; overflow: hidden; background: #ffffff;
  }
  .flyer {
    position: relative; width: 947px; height: 1200px; overflow: hidden;
    font-family: "Open Sans", Arial, sans-serif; color: var(--white);
  }
  .flyer-art { position: absolute; inset: 0; }
  .headline {
    position: absolute; left: 89px; top: 30px; width: 810px;
    font-family: "Roboto Condensed", "Arial Narrow", sans-serif; font-weight: 700;
    font-size: 66px; line-height: 1; color: var(--ink); white-space: nowrap; letter-spacing: 0.5px;
  }
  .tagline {
    position: absolute; right: 62px; top: 126px;
    font-family: "Roboto Condensed", "Arial Narrow", sans-serif; font-weight: 700;
    font-size: 36px; line-height: 1; color: var(--ink-soft); white-space: nowrap;
  }
  .school-mark {
    position: absolute; left: 48px; top: 592px; display: flex; align-items: center; gap: 14px;
  }
  .school-mark-dot { width: 56px; height: 56px; border-radius: 50%; background: var(--gold); }
  .school-mark-name {
    font-family: "Open Sans", Arial, sans-serif; font-weight: 700; font-size: 24px; line-height: 1.15;
    color: var(--gold);
  }
  .council {
    position: absolute; left: 262px; top: 621px;
    font-family: "Roboto Condensed", "Arial Narrow", sans-serif; font-weight: 700;
    font-size: 26px; line-height: 34px;
  }
  .findings {
    position: absolute; left: 56px; top: 757px; width: 420px; list-style: none;
    font-size: 17.5px; line-height: 22px;
    display: flex; flex-direction: column; gap: 9px;
  }
  .findings li { position: relative; padding-left: 32px; }
  .findings li::before {
    content: ""; position: absolute; left: 0; top: 2px; width: 18px; height: 18px;
    border-radius: 50%; background: var(--gold);
  }
  .findings li::after {
    content: ""; position: absolute; left: 5px; top: 6px; width: 7px; height: 4px;
    border-left: 2.5px solid var(--maroon); border-bottom: 2.5px solid var(--maroon);
    transform: rotate(-45deg);
  }
  .academy-note {
    position: absolute; left: 600px; top: 718px; width: 330px; transform: translateX(-50%);
    left: 765px; text-align: center;
    font-family: "Open Sans", Arial, sans-serif; font-weight: 700; font-size: 24px; line-height: 34px;
    color: var(--gold);
  }
  .good-school {
    position: absolute; right: 10px; top: 912px;
    font-family: "Roboto Condensed", "Arial Narrow", sans-serif; font-weight: 700;
    font-size: 35px; line-height: 1; white-space: nowrap;
  }
  .partnership {
    position: absolute; right: 10px; top: 968px; width: 360px; text-align: right;
    font-size: 18px; line-height: 25px; color: var(--blush);
  }
  .trust-card {
    position: absolute; left: 533px; top: 1070px; width: 385px; height: 93px;
    background: var(--white); border-radius: 3px;
    display: flex; align-items: center; justify-content: center; gap: 14px;
  }
  .trust-card-square { width: 34px; height: 34px; background: #8ea853; }
  .trust-card-name {
    font-family: "Open Sans", Arial, sans-serif; font-weight: 600; font-size: 21px; line-height: 1.15;
    color: #5f6a72;
  }
  .web-links {
    position: absolute; left: 52px; top: 1102px;
    font-family: "Open Sans", Arial, sans-serif; font-weight: 700; font-size: 25px; line-height: 36px;
  }
</style>
</head>
<body>
<main class="flyer">
  <svg class="flyer-art" width="947" height="1200" viewBox="0 0 947 1200" aria-hidden="false">
    <defs>
      <linearGradient id="sky" x1="0" y1="0" x2="0.3" y2="1">
        <stop offset="0" stop-color="var(--sky-top)"/>
        <stop offset="1" stop-color="var(--sky-bottom)"/>
      </linearGradient>
      <linearGradient id="photoTones" x1="0" y1="0" x2="1" y2="0.4">
        <stop offset="0" stop-color="#c7b6a3"/>
        <stop offset="0.45" stop-color="#ece6e0"/>
        <stop offset="0.8" stop-color="#d7d2cf"/>
        <stop offset="1" stop-color="#7f98b5"/>
      </linearGradient>
      <linearGradient id="maroonFill" x1="0" y1="0" x2="0" y2="1">
        <stop offset="0" stop-color="var(--maroon)"/>
        <stop offset="1" stop-color="var(--maroon-deep)"/>
      </linearGradient>
    </defs>
    <rect class="sky-band" x="0" y="0" width="947" height="560" fill="url(#sky)"/>
    <path class="pupils-photo" role="img" aria-label="Photograph of six smiling pupils in white shirts and striped ties standing together in a school library"
          d="M0,282 C260,205 560,300 947,192 L947,530 C640,560 330,470 0,505 Z" fill="url(#photoTones)"/>
    <path class="top-swoosh" d="M0,272 C260,192 560,292 947,180" fill="none" stroke="var(--swoosh)" stroke-width="14"/>
    <path class="top-swoosh-light" d="M0,262 C260,182 560,282 947,168" fill="none" stroke="var(--swoosh-light)" stroke-width="6"/>
    <path class="bottom-swoosh" d="M0,492 C320,455 620,548 947,498" fill="none" stroke="var(--swoosh-light)" stroke-width="12"/>
    <path class="bottom-swoosh-dark" d="M0,500 C320,466 620,558 947,508" fill="none" stroke="var(--swoosh)" stroke-width="10"/>
    <path class="maroon-panel" d="M0,506 C320,474 620,566 947,514 L947,1200 L0,1200 Z" fill="url(#maroonFill)"/>
  </svg>

  <h1 class="headline">Growing Bright Minds</h1>
  <p class="tagline">The Quality of Teaching is Good</p>

  <div class="school-mark">
    <span class="school-mark-dot"></span>
    <span class="school-mark-name">Thornbury<br>School</span>
  </div>

  <p class="council">Linford Core Council,<br>Active Boys Linford</p>

  <ul class="findings">
    <li>Pupils achievement has improved very quickly this year'</li>
    <li>Pupils make a strong start in the school</li>
    <li>The behaviour of pupils is good</li>
    <li>Reference to Edrevue rating of Good. Feb 2014</li>
    <li>This is a very different school to the one that existed at the time of the previous inspection</li>
    <li>The Executive Headteacher and leadership team have skilfully steered the school's recovery and galvanised staff at all levels to work as a team</li>
  </ul>

  <p class="academy-note">Reference to the fact we are converting to academy status on 1st April 2014 with The Harwick BRIDGE Academy Trust</p>

  <h2 class="good-school">This is a Good School</h2>
  <p class="partnership">Reference to the partnership with Colsworth Primary School which has bought recent, quick success</p>

  <div class="trust-card">
    <span class="trust-card-square"></span>
    <span class="trust-card-name">Harwick BRIDGE<br>Academy Trust</span>
  </div>

  <p class="web-links">www.harwickbridge.example<br>www.thornburyprimary.example</p>
</main>
</body>
</html>
```